依頼詳細
チラシを持参してもらったお客様限定のお試し価格の案内チラシを作成したいと思います。
普段のお客様ですと、お店の高級感から敷居が高いように感じられがちですが、
今回は、少しライトな層を狙えるようなイメージを持っています。
記載項目
◆焼肉バー ミヨコ

・ぐるめ帳ページ
https://gurumecho.example/aichi/B4812/B481207/58194630/

・Picstream
https://www.picstream.example/miyoko_yakiniku_bar/
サイズ
A5
ページ数
片面
希望イメージ
シンプル 複雑
単色 カラフル
暗い 明るい
日常 高級
遊び心 厳粛
未来的 伝統的
女性的 男性的
希望する色
黄・オレンジ系、無彩色系
納品ファイル
• 高解像度JPG (.jpg)
• イラストレーター形式 (.ai)
補足説明

```html
<!DOCTYPE html>
<html lang="ja">
<head>
<meta charset="utf-8">
<title>焼肉バー ミヨコ お試しコース</title>
<link rel="stylesheet" href="https://fonts.googleapis.com/css2?family=Noto+Serif+JP:wght@400;600;700;900&family=Cormorant+Garamond:wght@500;600&display=swap">
<style>
:root{
  --ink:#1d1a19;
  --red:#c8102e;
  --ribbon:#7a1a1c;
  --marble:#f3f2f0;
  --line:#3a3634;
  --meat-dark:#5a1d1f;
  --meat-mid:#a2383a;
  --meat-light:#c96a66;
  --photo-dark:#2a2220;
}
*{margin:0;padding:0;box-sizing:border-box}
html,body{width:844px;height:1200px;overflow:hidden;background:#fff}
.flyer{position:relative;width:844px;height:1200px;overflow:hidden;
  background:
    radial-gradient(ellipse at 30% 40%,rgba(255,255,255,.9),transparent 60%),
    linear-gradient(160deg,var(--marble) 0%,#e9e7e4 45%,var(--marble) 100%);
  font-family:"Noto Serif JP",serif;color:var(--ink)}
.photo{position:absolute}
.photo--top-left{left:0;top:0;width:300px;height:300px;
  background:radial-gradient(ellipse at 40% 45%,var(--meat-light),var(--meat-mid) 45%,var(--meat-dark) 85%);
  clip-path:polygon(0 0,100% 0,72% 100%,0 100%)}
.photo--top-right{right:0;top:0;width:310px;height:300px;
  background:radial-gradient(ellipse at 60% 40%,var(--meat-light),var(--meat-mid) 45%,var(--meat-dark) 85%);
  clip-path:polygon(0 0,100% 0,100% 100%,30% 100%)}
.photo--bottom{left:0;bottom:0;width:844px;height:110px;
  background:linear-gradient(90deg,var(--photo-dark),#6b3a30 30%,#3a2b26 55%,#7a4a3c 80%,var(--photo-dark))}
.ribbon{position:absolute;left:0;top:0;width:330px;height:52px;background:var(--ribbon);
  clip-path:polygon(0 0,100% 0,92% 100%,0 100%);
  color:#fff;font-size:17px;letter-spacing:.12em;line-height:52px;padding-left:40px}
.brand{position:absolute;left:0;right:0;top:160px;text-align:center}
.brand__dot{display:block;width:44px;height:44px;border-radius:50%;background:var(--ink);margin:0 auto 18px}
.brand__name{font-family:"Cormorant Garamond",serif;font-weight:600;font-size:44px;letter-spacing:.22em;color:var(--ink)}
.lead{position:absolute;left:50px;top:345px;font-weight:900;font-size:36px;line-height:1.5;letter-spacing:.02em}
.lead__num{color:var(--red);font-size:50px}
.course-title{position:absolute;left:48px;top:462px;font-weight:700;font-size:80px;line-height:1.2;color:var(--red);letter-spacing:.04em}
.price{position:absolute;left:50px;top:590px;height:150px;color:var(--red);display:flex;align-items:baseline;line-height:1}
.price__tax{font-size:26px;font-weight:700;margin-right:10px}
.price__yen{font-size:96px;font-weight:700;font-family:"Cormorant Garamond",serif;font-style:italic}
.price__num{font-size:140px;font-weight:600;font-family:"Cormorant Garamond",serif;font-style:italic;letter-spacing:.02em}
.note{position:absolute;left:50px;top:775px;width:570px;font-size:17px;line-height:1.9;font-weight:600}
.menu{position:absolute;left:633px;top:418px;width:190px;height:432px;border:1.5px solid var(--line);
  background:rgba(255,255,255,.55);padding:20px 16px;display:flex;flex-direction:column}
.menu__title{font-size:18px;font-weight:700;line-height:1.45;margin-bottom:14px}
.menu__list{list-style:none;font-size:16px;font-weight:600;line-height:1.85}
.menu__foot{margin-top:auto;font-size:13px;line-height:1.65;font-weight:600}
.divider{position:absolute;left:40px;top:890px;width:570px;height:1.5px;background:var(--line)}
.info{position:absolute;left:40px;top:906px;width:600px}
.info__catch{font-size:21px;font-weight:700;letter-spacing:.04em}
.info__row{display:flex;align-items:baseline;margin-top:6px}
.info__name{font-size:19px;font-weight:700}
.info__name b{font-size:38px;font-weight:900;margin-left:10px;letter-spacing:.08em}
.info__tel{margin-left:26px;font-size:34px;font-weight:700;letter-spacing:.02em;display:flex;align-items:center}
.info__tel svg{margin-right:6px}
.info__meta{display:flex;gap:28px;margin-top:8px;font-size:14px;font-weight:600}
</style>
</head>
<body>
<div class="flyer">
  <div class="photo photo--top-left" role="img" aria-label="霜降り和牛ステーキ肉の写真"></div>
  <div class="photo photo--top-right" role="img" aria-label="厚切りの赤身肉の写真"></div>
  <div class="ribbon">このチラシをご持参ください</div>

  <div class="brand">
    <span class="brand__dot"></span>
    <span class="brand__name">MIYOKO</span>
  </div>

  <p class="lead">今から<span class="lead__num">30</span>分以内に<br>ご来店のお客様限定コース!?</p>
  <h1 class="course-title">お試しコース</h1>
  <div class="price"><span class="price__tax">税込</span><span class="price__yen">¥</span><span class="price__num">980</span></div>

  <aside class="menu">
    <h2 class="menu__title">お試し<br>コースメニュー</h2>
    <ul class="menu__list">
      <li>厚切りネギ塩タン</li>
      <li>黒毛和牛カルビ</li>
      <li>ミヨコサラダ</li>
      <li>本日の赤身</li>
      <li>特選タレハラミ</li>
      <li>テールの土瓶蒸し</li>
      <li>和牛ホルモン</li>
      <li>ライス</li>
    </ul>
    <p class="menu__foot">お試しコースの為<br>少量でのご提供と<br>なります。</p>
  </aside>

  <p class="note">チラシをお持ちのお客様のみの限定コースでございます。<br>ご来店の際、お持ち頂きスタッフにご提示ください。</p>

  <div class="divider"></div>

  <div class="info">
    <p class="info__catch">錦でお得に贅沢なひとときを</p>
    <div class="info__row">
      <span class="info__name">焼肉バー<b>ミヨコ</b></span>
      <span class="info__tel">
        <svg width="26" height="26" viewBox="0 0 24 24" aria-hidden="true"><path fill="#1d1a19" d="M6.6 10.8a15.5 15.5 0 0 0 6.6 6.6l2.2-2.2a1 1 0 0 1 1-.25 11.4 11.4 0 0 0 3.6.57 1 1 0 0 1 1 1V20a1 1 0 0 1-1 1A17 17 0 0 1 3 4a1 1 0 0 1 1-1h3.5a1 1 0 0 1 1 1c0 1.25.2 2.45.57 3.57a1 1 0 0 1-.25 1z"/></svg>
        TEL.052-903-4176
      </span>
    </div>
    <div class="info__meta">
      <span>(月〜土) 18:00〜翌5:00 (L.O. 翌4:00)</span>
      <span>愛知県名古屋市中区錦5-8-12 月見ビル3F</span>
    </div>
  </div>

  <div class="photo photo--bottom" role="img" aria-label="焼肉料理と店内の写真"></div>
</div>
</body>
</html>
```